SEASONING LABEL RE-DESIGN

We are looking for someone to redesign our clients seasoning labels to look more professional and store ready

Please see attached details..

Target Market(s)

People who cook

Industry/Entity Type

Food Industry

Font styles to use
Sans Serif

Requirements
Must have
• Bold but FUN !

```html
<!DOCTYPE html>
<html lang="en">
<head>
<meta charset="utf-8">
<title>Ridgeback Seasoning – Label Range</title>
<link href="https://fonts.googleapis.com/css2?family=Alfa+Slab+One&family=Roboto+Slab:wght@700;900&family=Arimo:wght@400;700&display=swap" rel="stylesheet">
<style>
  :root{
    --canvas:#ffffff;
    --panel:#151515;
    --panel-hi:#262626;
    --ink:#ffffff;
    --logo:#efe3a0;
    --stripe:#8a8a8a;
    --badge:#6cbf3c;
    --red:#f42b2b;
    --brisket:#5b2c10;
    --blue:#1e8fe6;
    --whisky:#a52a2a;
    --orange:#f7922a;
    --seafood:#8b3f0d;
    --butter:#f4cd6e;
    --cajun:#d6282c;
    --allin:#1d4d21;
    --lemon:#f6c52e;
    --bbq:#a8170f;
    --jerk:#6ccf5a;
  }
  *{margin:0;padding:0;box-sizing:border-box}
  html,body{width:1200px;height:1200px;overflow:hidden;background:var(--canvas)}
  .sheet{position:relative;width:1200px;height:1200px}

  .label{position:absolute;width:322px;height:182px;background:var(--edge);font-family:"Roboto Slab",serif;color:var(--ink)}
  .label .panel{position:absolute;inset:6px;background:radial-gradient(ellipse at 50% 40%,var(--panel-hi),var(--panel) 75%)}

  .nutrition{position:absolute;left:8px;top:8px;width:52px;height:92px;background:#fff;overflow:hidden}
  .nutrition .rot{position:absolute;left:50%;top:50%;width:88px;height:48px;transform:translate(-50%,-50%) rotate(-90deg);
    font-family:Arimo,sans-serif;color:#000;font-size:3.6px;line-height:1.35;padding:2px}
  .nutrition .head{border-bottom:.4px solid #000;font-weight:700;display:flex;justify-content:space-between}
  .nutrition table{width:100%;border-collapse:collapse}
  .nutrition td{padding:0}
  .nutrition td:nth-child(2),.nutrition td:nth-child(3){text-align:right}

  .contains{position:absolute;left:8px;top:103px;width:52px;font-family:Arimo,sans-serif;font-size:3.6px;line-height:1.3;text-align:justify;color:#ddd}
  .contains b{display:block;font-size:4px;color:#fff}

  .brand{position:absolute;left:98px;top:16px;width:130px;text-align:center;font-family:"Alfa Slab One",serif;color:var(--logo);line-height:.95}
  .brand .name{font-size:17px;letter-spacing:.5px}
  .brand .sub{font-size:10px;letter-spacing:1px}
  .brand-dot{position:absolute;left:156px;top:54px;width:14px;height:14px;border-radius:50%;background:var(--logo)}

  .badge{position:absolute;left:181px;top:60px;width:36px;height:36px;border-radius:50%;background:var(--badge);border:1.5px solid #fff}

  .stripe{position:absolute;left:82px;top:90px;width:160px;height:5px;background:var(--stripe)}
  .ribbon{position:absolute;left:82px;top:96px;width:160px;height:51px;background:var(--ribbon);
    clip-path:polygon(0 0,100% 0,100% 38%,96% 50%,100% 62%,100% 100%,0 100%,0 62%,4% 50%,0 38%);
    display:flex;align-items:center;justify-content:center;text-align:center}
  .ribbon::before,.ribbon::after{content:"★";position:absolute;top:50%;transform:translateY(-50%);font-size:9px;color:#fff}
  .ribbon::before{left:14px}.ribbon::after{right:14px}
  .ribbon .title{font-family:"Alfa Slab One",serif;line-height:.95;color:#fff}
  .title .big{display:block;font-size:19px;letter-spacing:.5px}
  .title .small{display:block;font-size:10px;letter-spacing:.6px}
  .title .mid{display:block;font-size:13px}
  .title .xl{display:block;font-size:24px}

  .footer{position:absolute;left:87px;top:155px;height:20px;display:flex;align-items:center;gap:3px;font-family:"Alfa Slab One",serif}
  .crafted{font-size:5.5px;line-height:.9}
  .crafted span{display:block;font-size:10px}
  .divider{width:1px;height:16px;background:#fff;margin:0 2px}
  .net{font-size:7px;line-height:.95;color:var(--ribbon-text,var(--edge))}
  .weight{font-size:17px;line-height:1}
  .weight small{font-size:6px}
  .founders{margin-left:6px;font-family:Arimo,sans-serif;font-size:4px;line-height:1.3;color:var(--ribbon-text,var(--edge))}
  .founders i{display:block;color:#fff;font-size:4.5px}

  .pitch{position:absolute;left:258px;top:8px;width:52px;font-size:4.6px;line-height:1.55;letter-spacing:.2px;font-weight:900}
  .pitch .lg{font-size:7.2px;letter-spacing:.3px}
  .url{position:absolute;left:258px;top:164px;font-size:3.8px;font-weight:700}
</style>
</head>
<body>
<main class="sheet">

<!-- Row 1 -->
<article class="label" style="left:59px;top:194px;--edge:var(--red);--ribbon:var(--red)">
  <div class="panel"></div>
  <div class="nutrition"><div class="rot"><div class="head"><span>Calories: 0</span><span>Serving Size: 1/4 Tsp 1g</span></div><table><tr><td>Per Serving</td><td>Grams</td><td>%DV</td></tr><tr><td>Total Fat</td><td>0</td><td>0.0%</td></tr><tr><td>Trans Fat</td><td>0</td><td>0.0%</td></tr><tr><td>Sodium</td><td>190</td><td>7.6%</td></tr><tr><td>Tot Carbs</td><td>&lt;1g</td><td>0.0%</td></tr><tr><td>Protein</td><td>0</td><td>0.0%</td></tr></table></div></div>
  <p class="contains"><b>Contains:</b>Dehydrated garlic, spices, celery, sugar, onion powder, salt, parsley and turmeric extracts.</p>
  <div class="brand"><div class="name">RIDGEBACK</div><div class="sub">SEASONING</div></div><span class="brand-dot"></span>
  <span class="badge" role="img" aria-label="Gluten free seal"></span>
  <div class="stripe"></div>
  <div class="ribbon"><div class="title"><span class="mid">PRIME</span><span class="big">RIB</span></div></div>
  <div class="footer"><div class="crafted">CRAFTED IN<span>TEXAS</span></div><div class="divider"></div><div class="net">NET<br>WT</div><div class="weight">5.5<small>oz</small></div><div class="founders">FOUNDERS :<i>Sam &amp; Nora Pell</i></div></div>
  <p class="pitch"><span class="lg">RIDGEBACK</span><br>SEASONING IS A LOW SODIUM SEASONINGS <span class="lg">COMPANY</span><br>PROVIDING 12 <span class="lg">UNIQUE</span><br>SEASONING BLENDS SURE TO "TICKLE THE TASTE BUDS" OF ANY PALLET WITHOUT THE HIGH SODIUM INTAKE!</p>
  <p class="url">RIDGEBACKFLAVOR.COM</p>
</article>

<article class="label" style="left:418px;top:194px;--edge:var(--red);--ribbon:var(--brisket)">
  <div class="panel"></div>
  <div class="nutrition"><div class="rot"><div class="head"><span>Calories: 0</span><span>Serving Size: 1/4 Tsp 1g</span></div><table><tr><td>Per Serving</td><td>Grams</td><td>%DV</td></tr><tr><td>Total Fat</td><td>0</td><td>0.0%</td></tr><tr><td>Trans Fat</td><td>0</td><td>0.0%</td></tr><tr><td>Sodium</td><td>272</td><td>10.9%</td></tr><tr><td>Tot Carbs</td><td>&lt;1g</td><td>0.0%</td></tr><tr><td>Protein</td><td>0</td><td>0.0%</td></tr></table></div></div>
  <p class="contains"><b>Contains:</b>Spices, celery, salt, sugar, paprika, onion, garlic, turmeric, cinnamon and food starch.</p>
  <div class="brand"><div class="name">RIDGEBACK</div><div class="sub">SEASONING</div></div><span class="brand-dot"></span>
  <span class="badge" role="img" aria-label="Gluten free seal"></span>
  <div class="stripe"></div>
  <div class="ribbon"><div class="title"><span class="big">HEART OF</span><span class="small">TEXAS BRISKET</span></div></div>
  <div class="footer"><div class="crafted">CRAFTED IN<span>TEXAS</span></div><div class="divider"></div><div class="net" style="color:var(--brisket)">NET<br>WT</div><div class="weight">6<small>oz</small></div><div class="founders" style="color:var(--brisket)">FOUNDERS :<i>Sam &amp; Nora Pell</i></div></div>
  <p class="pitch"><span class="lg">RIDGEBACK</span><br>SEASONING IS A LOW SODIUM SEASONINGS <span class="lg">COMPANY</span><br>PROVIDING 12 <span class="lg">UNIQUE</span><br>SEASONING BLENDS SURE TO "TICKLE THE TASTE BUDS" OF ANY PALLET WITHOUT THE HIGH SODIUM INTAKE!</p>
  <p class="url">RIDGEBACKFLAVOR.COM</p>
</article>

<article class="label" style="left:778px;top:194px;--edge:var(--blue);--ribbon:var(--blue)">
  <div class="panel"></div>
  <div class="nutrition"><div class="rot"><div class="head"><span>Calories: 0</span><span>Serving Size: 1/4 Tsp 1g</span></div><table><tr><td>Per Serving</td><td>Grams</td><td>%DV</td></tr><tr><td>Total Fat</td><td>0</td><td>0.0%</td></tr><tr><td>Trans Fat</td><td>0</td><td>0.0%</td></tr><tr><td>Sodium</td><td>132</td><td>5.3%</td></tr><tr><td>Tot Carbs</td><td>&lt;1g</td><td>0.0%</td></tr><tr><td>Protein</td><td>0</td><td>0.0%</td></tr></table></div></div>
  <p class="contains"><b>Contains:</b>Onion, garlic, spices, dehydrated parsley, salt, and silicon dioxide to prevent caking.</p>
  <div class="brand"><div class="name">RIDGEBACK</div><div class="sub">SEASONING</div></div><span class="brand-dot"></span>
  <span class="badge" role="img" aria-label="Gluten free seal"></span>
  <div class="stripe"></div>
  <div class="ribbon"><div class="title"><span class="xl">RANCH</span></div></div>
  <div class="footer"><div class="crafted">CRAFTED IN<span>TEXAS</span></div><div class="divider"></div><div class="net">NET<br>WT</div><div class="weight">5.5<small>oz</small></div><div class="founders">FOUNDERS :<i>Sam &amp; Nora Pell</i></div></div>
  <p class="pitch"><span class="lg">RIDGEBACK</span><br>SEASONING IS A LOW SODIUM SEASONINGS <span class="lg">COMPANY</span><br>PROVIDING 12 <span class="lg">UNIQUE</span><br>SEASONING BLENDS SURE TO "TICKLE THE TASTE BUDS" OF ANY PALLET WITHOUT THE HIGH SODIUM INTAKE!</p>
  <p class="url">RIDGEBACKFLAVOR.COM</p>
</article>

<!-- Row 2 -->
<article class="label" style="left:59px;top:391px;--edge:var(--whisky);--ribbon:var(--whisky);--ribbon-text:var(--red)">
  <div class="panel"></div>
  <div class="nutrition"><div class="rot"><div class="head"><span>Calories: 0</span><span>Serving Size: 1/4 Tsp 1g</span></div><table><tr><td>Per Serving</td><td>Grams</td><td>%DV</td></tr><tr><td>Total Fat</td><td>0</td><td>0.0%</td></tr><tr><td>Trans Fat</td><td>0</td><td>0.0%</td></tr><tr><td>Sodium</td><td>163</td><td>6.5%</td></tr><tr><td>Tot Carbs</td><td>&lt;1g</td><td>0.0%</td></tr><tr><td>Protein</td><td>0</td><td>0.0%</td></tr></table></div></div>
  <p class="contains"><b>Contains:</b>Garlic, spices, celery, salt, sugar, bourbon flavor, onion, parsley and soy oil.</p>
  <div class="brand"><div class="name">RIDGEBACK</div><div class="sub">SEASONING</div></div><span class="brand-dot"></span>
  <span class="badge" role="img" aria-label="Gluten free seal"></span>
  <div class="stripe"></div>
  <div class="ribbon"><div class="title"><span class="big">WHISKY</span><span class="big">STEAK</span></div></div>
  <div class="footer"><div class="crafted">CRAFTED IN<span>TEXAS</span></div><div class="divider"></div><div class="net">NET<br>WT</div><div class="weight">5.5<small>oz</small></div><div class="founders">FOUNDERS :<i>Sam &amp; Nora Pell</i></div></div>
  <p class="pitch"><span class="lg">RIDGEBACK</span><br>SEASONING IS A LOW SODIUM SEASONINGS <span class="lg">COMPANY</span><br>PROVIDING 12 <span class="lg">UNIQUE</span><br>SEASONING BLENDS SURE TO "TICKLE THE TASTE BUDS" OF ANY PALLET WITHOUT THE HIGH SODIUM INTAKE!</p>
  <p class="url">RIDGEBACKFLAVOR.COM</p>
</article>

<article class="label" style="left:418px;top:391px;--edge:var(--orange);--ribbon:var(--orange)">
  <div class="panel"></div>
  <div class="nutrition"><div class="rot"><div class="head"><span>Calories: 0</span><span>Serving Size: 1/4 Tsp 1g</span></div><table><tr><td>Per Serving</td><td>Grams</td><td>%DV</td></tr><tr><td>Total Fat</td><td>0</td><td>0.0%</td></tr><tr><td>Trans Fat</td><td>0</td><td>0.0%</td></tr><tr><td>Sodium</td><td>162</td><td>6.5%</td></tr><tr><td>Tot Carbs</td><td>&lt;1g</td><td>0.0%</td></tr><tr><td>Protein</td><td>0</td><td>0.0%</td></tr></table></div></div>
  <p class="contains"><b>Contains:</b>Garlic, sugar, spices, salt, onion, paprika, turmeric, and soy oil to prevent caking.</p>
  <div class="brand"><div class="name">RIDGEBACK</div><div class="sub">SEASONING</div></div><span class="brand-dot"></span>
  <span class="badge" role="img" aria-label="Gluten free seal"></span>
  <div class="stripe"></div>
  <div class="ribbon"><div class="title"><span class="big">DRUNKEN</span><span class="big">CHICKEN</span></div></div>
  <div class="footer"><div class="crafted">CRAFTED IN<span>TEXAS</span></div><div class="divider"></div><div class="net">NET<br>WT</div><div class="weight">5.5<small>oz</small></div><div class="founders">FOUNDERS :<i>Sam &amp; Nora Pell</i></div></div>
  <p class="pitch"><span class="lg">RIDGEBACK</span><br>SEASONING IS A LOW SODIUM SEASONINGS <span class="lg">COMPANY</span><br>PROVIDING 12 <span class="lg">UNIQUE</span><br>SEASONING BLENDS SURE TO "TICKLE THE TASTE BUDS" OF ANY PALLET WITHOUT THE HIGH SODIUM INTAKE!</p>
  <p class="url">RIDGEBACKFLAVOR.COM</p>
</article>

<article class="label" style="left:778px;top:391px;--edge:var(--seafood);--ribbon:var(--seafood)">
  <div class="panel"></div>
  <div class="nutrition"><div class="rot"><div class="head"><span>Calories: 0</span><span>Serving Size: 1/4 Tsp 1g</span></div><table><tr><td>Per Serving</td><td>Grams</td><td>%DV</td></tr><tr><td>Total Fat</td><td>0</td><td>0.0%</td></tr><tr><td>Trans Fat</td><td>0</td><td>0.0%</td></tr><tr><td>Sodium</td><td>202</td><td>8.0%</td></tr><tr><td>Tot Carbs</td><td>&lt;1g</td><td>0.0%</td></tr><tr><td>Protein</td><td>0</td><td>0.0%</td></tr></table></div></div>
  <p class="contains"><b>Contains:</b>Spices, celery, sage, garlic, sugar, salt, paprika, mustard, citric acid and lemon.</p>
  <div class="brand"><div class="name">RIDGEBACK</div><div class="sub">SEASONING</div></div><span class="brand-dot"></span>
  <span class="badge" role="img" aria-label="Gluten free seal"></span>
  <div class="stripe"></div>
  <div class="ribbon"><div class="title"><span class="big">RIDGEBACK</span><span class="small">SEAFOOD BLEND</span></div></div>
  <div class="footer"><div class="crafted">CRAFTED IN<span>TEXAS</span></div><div class="divider"></div><div class="net">NET<br>WT</div><div class="weight">7<small>oz</small></div><div class="founders">FOUNDERS :<i>Sam &amp; Nora Pell</i></div></div>
  <p class="pitch"><span class="lg">RIDGEBACK</span><br>SEASONING IS A LOW SODIUM SEASONINGS <span class="lg">COMPANY</span><br>PROVIDING 12 <span class="lg">UNIQUE</span><br>SEASONING BLENDS SURE TO "TICKLE THE TASTE BUDS" OF ANY PALLET WITHOUT THE HIGH SODIUM INTAKE!</p>
  <p class="url">RIDGEBACKFLAVOR.COM</p>
</article>

<!-- Row 3 -->
<article class="label" style="left:59px;top:588px;--edge:var(--butter);--ribbon:var(--butter)">
  <div class="panel"></div>
  <div class="nutrition"><div class="rot"><div class="head"><span>Calories: 0</span><span>Serving Size: 1/4 Tsp 1g</span></div><table><tr><td>Per Serving</td><td>Grams</td><td>%DV</td></tr><tr><td>Total Fat</td><td>0</td><td>0.0%</td></tr><tr><td>Trans Fat</td><td>0</td><td>0.0%</td></tr><tr><td>Sodium</td><td>136</td><td>5.4%</td></tr><tr><td>Tot Carbs</td><td>&lt;1g</td><td>0.0%</td></tr><tr><td>Protein</td><td>0</td><td>0.0%</td></tr></table></div></div>
  <p class="contains"><b>Contains:</b>Garlic, sugar, onion, spices, butter flavor, salt, garlic oil, and soy oil.</p>
  <div class="brand"><div class="name">RIDGEBACK</div><div class="sub">SEASONING</div></div><span class="brand-dot"></span>
  <span class="badge" role="img" aria-label="Gluten free seal"></span>
  <div class="stripe"></div>
  <div class="ribbon"><div class="title"><span class="big">GARLIC</span><span class="big">BUTTER</span></div></div>
  <div class="footer"><div class="crafted">CRAFTED IN<span>TEXAS</span></div><div class="divider"></div><div class="net">NET<br>WT</div><div class="weight">5.5<small>oz</small></div><div class="founders">FOUNDERS :<i>Sam &amp; Nora Pell</i></div></div>
  <p class="pitch"><span class="lg">RIDGEBACK</span><br>SEASONING IS A LOW SODIUM SEASONINGS <span class="lg">COMPANY</span><br>PROVIDING 12 <span class="lg">UNIQUE</span><br>SEASONING BLENDS SURE TO "TICKLE THE TASTE BUDS" OF ANY PALLET WITHOUT THE HIGH SODIUM INTAKE!</p>
  <p class="url">RIDGEBACKFLAVOR.COM</p>
</article>

<article class="label" style="left:418px;top:588px;--edge:var(--cajun);--ribbon:var(--cajun)">
  <div class="panel"></div>
  <div class="nutrition"><div class="rot"><div class="head"><span>Calories: 0</span><span>Serving Size: 1/4 Tsp 1g</span></div><table><tr><td>Per Serving</td><td>Grams</td><td>%DV</td></tr><tr><td>Total Fat</td><td>0</td><td>0.0%</td></tr><tr><td>Trans Fat</td><td>0</td><td>0.0%</td></tr><tr><td>Sodium</td><td>253</td><td>10.1%</td></tr><tr><td>Tot Carbs</td><td>&lt;1g</td><td>0.0%</td></tr><tr><td>Protein</td><td>0</td><td>0.0%</td></tr></table></div></div>
  <p class="contains"><b>Contains:</b>Spices, paprika, celery, onion, garlic powder, salt, sugar, food starch, and paprika extracts.</p>
  <div class="brand"><div class="name">RIDGEBACK</div><div class="sub">SEASONING</div></div><span class="brand-dot"></span>
  <span class="badge" role="img" aria-label="Gluten free seal"></span>
  <div class="stripe"></div>
  <div class="ribbon"><div class="title"><span class="xl">CAJUN</span><span class="mid">SEASONING</span></div></div>
  <div class="footer"><div class="crafted">CRAFTED IN<span>TEXAS</span></div><div class="divider"></div><div class="net">NET<br>WT</div><div class="weight">6<small>oz</small></div><div class="founders">FOUNDERS :<i>Sam &amp; Nora Pell</i></div></div>
  <p class="pitch"><span class="lg">RIDGEBACK</span><br>SEASONING IS A LOW SODIUM SEASONINGS <span class="lg">COMPANY</span><br>PROVIDING 12 <span class="lg">UNIQUE</span><br>SEASONING BLENDS SURE TO "TICKLE THE TASTE BUDS" OF ANY PALLET WITHOUT THE HIGH SODIUM INTAKE!</p>
  <p class="url">RIDGEBACKFLAVOR.COM</p>
</article>

<article class="label" style="left:778px;top:588px;--edge:var(--allin);--ribbon:var(--allin)">
  <div class="panel"></div>
  <div class="nutrition"><div class="rot"><div class="head"><span>Calories: 0</span><span>Serving Size: 1/4 Tsp 1g</span></div><table><tr><td>Per Serving</td><td>Grams</td><td>%DV</td></tr><tr><td>Total Fat</td><td>0</td><td>0.0%</td></tr><tr><td>Trans Fat</td><td>0</td><td>0.0%</td></tr><tr><td>Sodium</td><td>198</td><td>8.0%</td></tr><tr><td>Tot Carbs</td><td>&lt;1g</td><td>0.0%</td></tr><tr><td>Protein</td><td>0</td><td>0.0%</td></tr></table></div></div>
  <p class="contains"><b>Contains:</b>Spices, celery, garlic, onion, sugar, brown sugar, paprika, salt, mustard, and parsley.</p>
  <div class="brand"><div class="name">RIDGEBACK</div><div class="sub">SEASONING</div></div><span class="brand-dot"></span>
  <span class="badge" role="img" aria-label="Gluten free seal"></span>
  <div class="stripe"></div>
  <div class="ribbon"><div class="title"><span class="xl">ALL-IN</span><span class="mid">SEASONING</span></div></div>
  <div class="footer"><div class="crafted">CRAFTED IN<span>TEXAS</span></div><div class="divider"></div><div class="net">NET<br>WT</div><div class="weight">7<small>oz</small></div><div class="founders">FOUNDERS :<i>Sam &amp; Nora Pell</i></div></div>
  <p class="pitch"><span class="lg">RIDGEBACK</span><br>SEASONING IS A LOW SODIUM SEASONINGS <span class="lg">COMPANY</span><br>PROVIDING 12 <span class="lg">UNIQUE</span><br>SEASONING BLENDS SURE TO "TICKLE THE TASTE BUDS" OF ANY PALLET WITHOUT THE HIGH SODIUM INTAKE!</p>
  <p class="url">RIDGEBACKFLAVOR.COM</p>
</article>

<!-- Row 4 -->
<article class="label" style="left:59px;top:785px;--edge:var(--lemon);--ribbon:var(--lemon)">
  <div class="panel"></div>
  <div class="nutrition"><div class="rot"><div class="head"><span>Calories: 0</span><span>Serving Size: 1/4 Tsp 1g</span></div><table><tr><td>Per Serving</td><td>Grams</td><td>%DV</td></tr><tr><td>Total Fat</td><td>0</td><td>0.0%</td></tr><tr><td>Trans Fat</td><td>0</td><td>0.0%</td></tr><tr><td>Sodium</td><td>267</td><td>10.7%</td></tr><tr><td>Tot Carbs</td><td>&lt;1g</td><td>0.0%</td></tr><tr><td>Protein</td><td>0</td><td>0.0%</td></tr></table></div></div>
  <p class="contains"><b>Contains:</b>Spice, citric acid, dehydrated onion, garlic, salt, sugar, celery seed, and lemon juice.</p>
  <div class="brand"><div class="name">RIDGEBACK</div><div class="sub">SEASONING</div></div><span class="brand-dot"></span>
  <span class="badge" role="img" aria-label="Gluten free seal"></span>
  <div class="stripe"></div>
  <div class="ribbon"><div class="title"><span class="big">LEMON</span><span class="big">PEPPER</span></div></div>
  <div class="footer"><div class="crafted">CRAFTED IN<span>TEXAS</span></div><div class="divider"></div><div class="net">NET<br>WT</div><div class="weight">6.5<small>oz</small></div><div class="founders">FOUNDERS :<i>Sam &amp; Nora Pell</i></div></div>
  <p class="pitch"><span class="lg">RIDGEBACK</span><br>SEASONING IS A LOW SODIUM SEASONINGS <span class="lg">COMPANY</span><br>PROVIDING 12 <span class="lg">UNIQUE</span><br>SEASONING BLENDS SURE TO "TICKLE THE TASTE BUDS" OF ANY PALLET WITHOUT THE HIGH SODIUM INTAKE!</p>
  <p class="url">RIDGEBACKFLAVOR.COM</p>
</article>

<article class="label" style="left:418px;top:785px;--edge:var(--cajun);--ribbon:var(--bbq);--ribbon-text:var(--red)">
  <div class="panel"></div>
  <div class="nutrition"><div class="rot"><div class="head"><span>Calories: 1</span><span>Serving Size: 1/4 Tsp 1g</span></div><table><tr><td>Per Serving</td><td>Grams</td><td>%DV</td></tr><tr><td>Total Fat</td><td>0</td><td>0.0%</td></tr><tr><td>Trans Fat</td><td>0</td><td>0.0%</td></tr><tr><td>Sodium</td><td>124</td><td>5.0%</td></tr><tr><td>Tot Carbs</td><td>&lt;1g</td><td>0.0%</td></tr><tr><td>Protein</td><td>0</td><td>0.0%</td></tr></table></div></div>
  <p class="contains"><b>Contains:</b>Spices, sugar, paprika, turmeric, dextrose, onion powder, salt, and soybean oil.</p>
  <div class="brand"><div class="name">RIDGEBACK</div><div class="sub">SEASONING</div></div><span class="brand-dot"></span>
  <span class="badge" role="img" aria-label="Gluten free seal"></span>
  <div class="stripe"></div>
  <div class="ribbon"><div class="title"><span class="xl" style="font-size:28px">BBQ</span></div></div>
  <div class="footer"><div class="crafted">CRAFTED IN<span>TEXAS</span></div><div class="divider"></div><div class="net">NET<br>WT</div><div class="weight">6<small>oz</small></div><div class="founders">FOUNDERS :<i>Sam &amp; Nora Pell</i></div></div>
  <p class="pitch"><span class="lg">RIDGEBACK</span><br>SEASONING IS A LOW SODIUM SEASONINGS <span class="lg">COMPANY</span><br>PROVIDING 12 <span class="lg">UNIQUE</span><br>SEASONING BLENDS SURE TO "TICKLE THE TASTE BUDS" OF ANY PALLET WITHOUT THE HIGH SODIUM INTAKE!</p>
  <p class="url">RIDGEBACKFLAVOR.COM</p>
</article>

<article class="label" style="left:778px;top:785px;--edge:var(--jerk);--ribbon:var(--jerk)">
  <div class="panel"></div>
  <div class="nutrition"><div class="rot"><div class="head"><span>Calories: 2</span><span>Serving Size: 1/4 Tsp 1g</span></div><table><tr><td>Per Serving</td><td>Grams</td><td>%DV</td></tr><tr><td>Total Fat</td><td>0</td><td>0.0%</td></tr><tr><td>Trans Fat</td><td>0</td><td>0.0%</td></tr><tr><td>Sodium</td><td>111</td><td>4.4%</td></tr><tr><td>Tot Carbs</td><td>1g</td><td>0.0%</td></tr><tr><td>Protein</td><td>0</td><td>0.0%</td></tr></table></div></div>
  <p class="contains"><b>Contains:</b>Sugar, spices, onion powder, and not more than 2% soy oil added.</p>
  <div class="brand"><div class="name">RIDGEBACK</div><div class="sub">SEASONING</div></div><span class="brand-dot"></span>
  <span class="badge" role="img" aria-label="Gluten free seal"></span>
  <div class="stripe"></div>
  <div class="ribbon"><div class="title"><span class="mid" style="font-size:15px">CARIBBEAN</span><span class="small">JERK SEASONING</span></div></div>
  <div class="footer"><div class="crafted">CRAFTED IN<span>TEXAS</span></div><div class="divider"></div><div class="net">NET<br>WT</div><div class="weight">6.5<small>oz</small></div><div class="founders">FOUNDERS :<i>Sam &amp; Nora Pell</i></div></div>
  <p class="pitch"><span class="lg">RIDGEBACK</span><br>SEASONING IS A LOW SODIUM SEASONINGS <span class="lg">COMPANY</span><br>PROVIDING 12 <span class="lg">UNIQUE</span><br>SEASONING BLENDS SURE TO "TICKLE THE TASTE BUDS" OF ANY PALLET WITHOUT THE HIGH SODIUM INTAKE!</p>
  <p class="url">RIDGEBACKFLAVOR.COM</p>
</article>

</main>
</body>
</html>
```